Gold Buyer Business Card

We are looking for a card that catches attention and that someone will remember. It should have a listing of items that we buy as well as a legal disclaimer which will be provided upon request. We have attached our company logo and a photo of a design that I liked for your reference but lets see what the crowd can come up with.
thanks and good luck!!

We Buy Gold & Silver;
Antique Jewelry
Bent/Broken Jewelry
Bracelets
Bullion
Coins
Chains
Dental Gold
Earrings
Rings
Scrap Gold
Silverware/Flatware
Used Jewelry

"Best Price Guaranteed"
Updates

Please use graphics of gold jewelry piles. I want some white in order for someone to write on.

Reason: I am looking for more designs with gold jewelry and coins on them. thanks

Industry/Entity Type

Legal

Requirements
Must have
• I would like this to have pictures of gold and silver. Maybe some jewelry in a pile. We are a company that buys scrap gold and jewelry. I would like to see some boldness, this card is a marketing tool and it should leave an impression.
Should not have
• These cards need to promote the company not an individual, no names on the card.

```html
<!DOCTYPE html>
<html lang="en">
<head>
<meta charset="utf-8">
<title>Harbor Point Gold Exchange – Business Card</title>
<link rel="stylesheet" href="https://fonts.googleapis.com/css2?family=Open+Sans:wght@400;600;700;800&display=swap">
<style>
  :root {
    --stage: #8c8e90;
    --card-black: #0b0b0b;
    --gold: #f2c230;
    --gold-deep: #d9a514;
    --gold-light: #ffd84a;
    --silver: #c9ccd1;
    --white: #ffffff;
    --ink: #111111;
  }
  * { box-sizing: border-box; margin: 0; padding: 0; }
  html, body {
    width: 1200px; height: 772px; overflow: hidden;
    background: var(--stage);
    font-family: "Open Sans", Arial, sans-serif;
  }
  .stage {
    width: 1200px; height: 772px;
    display: flex; align-items: center; justify-content: center; gap: 40px;
  }
  .card {
    position: relative;
    width: 540px; height: 309px;
    background: var(--card-black);
    overflow: hidden;
    color: var(--white);
  }
  .brand-name {
    position: absolute; left: 50%; transform: translateX(-50%);
    width: 400px;
    font-weight: 800; color: var(--gold);
    text-transform: uppercase; text-align: center;
    line-height: 1.05; letter-spacing: 0.5px;
  }
  .card-front .brand-name { top: 26px; font-size: 28px; }
  .card-back .brand-name { top: 30px; font-size: 24px; }

  /* Front: list of items bought */
  .buy-heading {
    position: absolute; top: 106px; left: 0; width: 100%;
    text-align: center; font-size: 14px; font-weight: 700;
    color: var(--gold); text-transform: uppercase; letter-spacing: 1px;
  }
  .buy-list {
    position: absolute; top: 134px; left: 40px; width: 460px;
    list-style: none;
    display: grid; grid-template-columns: repeat(3, 1fr);
    grid-auto-flow: column; grid-template-rows: repeat(4, 19px);
    font-size: 12px; line-height: 19px;
  }
  .buy-list li::before {
    content: ""; display: inline-block; width: 5px; height: 5px;
    background: var(--gold); border-radius: 50%;
    margin-right: 7px; vertical-align: middle;
  }
  .tagline {
    position: absolute; bottom: 26px; left: 0; width: 100%;
    text-align: center; font-size: 15px; font-weight: 700; color: var(--gold);
  }

  /* Back */
  .address {
    position: absolute; top: 104px; left: 34px;
    font-size: 12px; line-height: 1.35; font-style: normal;
  }
  .jewelry-pile {
    position: absolute; top: 96px; right: 34px;
    width: 170px; height: 96px; border-radius: 6px;
    background: radial-gradient(ellipse at 35% 60%, var(--gold-light) 0%, var(--gold) 35%, var(--gold-deep) 60%, transparent 78%),
                radial-gradient(ellipse at 75% 55%, var(--silver) 0%, #8f939a 45%, transparent 75%),
                #1c1a14;
  }
  .gold-wave { position: absolute; left: 0; bottom: 0; width: 540px; height: 309px; }
  .contacts {
    position: absolute; right: 34px; top: 206px;
    list-style: none; font-size: 12px; line-height: 1.55;
  }
  .contacts li { display: flex; align-items: center; justify-content: flex-end; gap: 6px; }
  .contacts svg { width: 10px; height: 10px; fill: var(--white); }
  .website {
    position: absolute; left: 92px; bottom: 34px;
    font-size: 11.5px; color: var(--ink); font-weight: 600;
    transform: rotate(10deg); transform-origin: left center;
  }
</style>
</head>
<body>
<main class="stage">

  <section class="card card-front" aria-label="Card front">
    <p class="brand-name">Harbor Point<br>Gold Exchange</p>
    <p class="buy-heading">We Buy Gold &amp; Silver</p>
    <ul class="buy-list">
      <li>Antique Jewelry</li>
      <li>Bent/Broken Jewelry</li>
      <li>Bracelets</li>
      <li>Bullion</li>
      <li>Coins</li>
      <li>Chains</li>
      <li>Dental Gold</li>
      <li>Earrings</li>
      <li>Rings</li>
      <li>Scrap Gold</li>
      <li>Silverware/Flatware</li>
      <li>Used Jewelry</li>
    </ul>
    <p class="tagline">“Best Price Guaranteed”</p>
  </section>

  <section class="card card-back" aria-label="Card back">
    <svg class="gold-wave" viewBox="0 0 540 309" aria-hidden="true">
      <defs>
        <linearGradient id="goldBand" x1="0" y1="0" x2="1" y2="0">
          <stop offset="0" stop-color="#d9a514"/>
          <stop offset="0.5" stop-color="#ffd84a"/>
          <stop offset="1" stop-color="#f2c230"/>
        </linearGradient>
      </defs>
      <path d="M0 198 C130 176 250 205 360 250 C420 275 480 300 540 309" fill="none" stroke="url(#goldBand)" stroke-width="2.5"/>
      <path d="M0 214 C120 196 230 224 330 268 C400 296 470 309 540 309 L0 309 Z" fill="url(#goldBand)"/>
      <path d="M0 262 C110 246 230 272 330 309" fill="none" stroke="#0b0b0b" stroke-width="5"/>
    </svg>

    <p class="brand-name">Harbor Point<br>Gold Exchange</p>

    <address class="address">
      214, 9th Floor,<br>Cedar Point<br>Road NWK
    </address>

    <div class="jewelry-pile" role="img" aria-label="Photo of a pile of gold and silver jewelry and coins"></div>

    <ul class="contacts">
      <li>012 555 0148
        <svg viewBox="0 0 10 10" aria-hidden="true"><path d="M2 0.5 L3.5 2.8 L2.6 3.8 C3.3 5.3 4.7 6.7 6.2 7.4 L7.2 6.5 L9.5 8 L8.5 9.6 C4.5 9.4 0.6 5.5 0.4 1.5 Z"/></svg>
      </li>
      <li>012 555 0149
        <svg viewBox="0 0 10 10" aria-hidden="true"><rect x="2.5" y="0" width="5" height="10" rx="1"/><rect x="3.3" y="1.2" width="3.4" height="6.3" fill="#0b0b0b"/></svg>
      </li>
      <li>hello@harborpointgold.com
        <svg viewBox="0 0 10 10" aria-hidden="true"><rect x="0" y="2" width="10" height="6.5"/><path d="M0.5 2.5 L5 6 L9.5 2.5" fill="none" stroke="#0b0b0b" stroke-width="1"/></svg>
      </li>
    </ul>

    <p class="website">www.harborpointgold.com</p>
  </section>

</main>
</body>
</html>
```